Website redesign and new logo

Hi we feel that the colours, layout and style along with the logo which is only text at the moment is poor. It seems to lack a quality and luxurious feel and we are about selling high end curtains. The text logo is hard to read as well in my opinion. We are looking for a overall revamp and an new logo. We want to maintain the main parts of the home page but happy to consider any ideas that will improve web traffic. It does not really reflect our achievements either of having curtains recently featured on lumen 6 tv.
The website in question is www.velmorrahangings.co.uk

```html
<!DOCTYPE html>
<html lang="en">
<head>
<meta charset="utf-8">
<title>Velmorra Hangings – Handmade Curtains</title>
<link rel="stylesheet" href="https://fonts.googleapis.com/css2?family=Arimo:wght@400;700&display=swap">
<style>
:root{
  --teal:#2a9d97;
  --teal-light:#4fbab3;
  --teal-dark:#1f7772;
  --band:#2e8b86;
  --footer:#23706c;
  --footer-deep:#1b5a57;
  --ink:#2b2b2b;
  --muted:#555;
  --paper:#ffffff;
  --grey:#f0f0f0;
}
*{box-sizing:border-box;margin:0;padding:0}
html,body{width:1200px;height:2471px;overflow:hidden}
body{position:relative;background:var(--paper);font-family:"Arimo",Arial,sans-serif;color:var(--ink)}
.abs{position:absolute}

/* hero */
.hero{left:0;top:0;width:1200px;height:673px;background:linear-gradient(180deg,#6d5a43 0%,#b9a58a 30%,#d8ccb8 60%,#efe8dc 85%,#ffffff 100%)}
.brand-box{left:494px;top:0;width:201px;height:110px;background:var(--teal);display:flex;align-items:center;justify-content:center;color:#fff;font-size:26px;font-weight:700;letter-spacing:1px;text-align:center;line-height:1.1}
.top-phone{right:110px;top:46px;color:#fff;font-size:14px;font-weight:700}
.top-mail{right:110px;top:66px;color:#fff;font-size:10px}
.nav{left:158px;top:124px;display:flex;gap:26px;color:#fff;font-size:14px;text-transform:uppercase}
.nav .active{font-weight:700}
.headline{left:275px;top:291px;width:659px;height:46px;background:var(--teal);color:#fff;font-size:36px;font-weight:700;text-align:center;line-height:46px}
.subline{left:275px;top:340px;width:659px;text-align:center;color:#fff;font-size:28px;font-weight:700;text-shadow:0 1px 3px rgba(0,0,0,.5)}

/* feature cards */
.card{background:linear-gradient(180deg,var(--teal-light),var(--teal) 60%,var(--teal-dark));color:#fff;text-align:center;box-shadow:0 14px 18px rgba(0,0,0,.25)}
.card-title{font-size:17px;line-height:1.25;padding:0 20px}
.card-photo{position:absolute}
.card-text{position:absolute;left:0;width:100%;font-size:12px;line-height:1.4;padding:0 24px}
.card-side{top:590px;width:289px;height:289px}
.card-side .card-title{padding-top:30px}
.card-side .card-photo{left:27px;top:96px;width:234px;height:110px}
.card-side .card-text{top:228px}
.card-mid{left:448px;top:541px;width:288px;height:379px}
.card-mid .card-title{padding-top:30px}
.card-mid .card-photo{left:27px;top:104px;width:234px;height:115px}
.card-name{position:absolute;top:232px;left:0;width:100%;font-size:14px;font-weight:700}
.card-mid .card-text{top:270px}

/* content */
.section-title{font-size:24px;color:var(--ink)}
.about{left:151px;top:1002px;width:481px}
.about p{font-size:13.5px;line-height:1.45;color:var(--muted);margin-top:18px}
.designer{left:654px;top:1002px}
.video{left:654px;top:1057px;width:370px;height:247px;background:linear-gradient(135deg,#d9d3cb,#8a7663 50%,#c9bfb2)}
.video-bar{left:654px;top:1282px;width:370px;height:22px;background:#1b1b1b}

/* areas */
.areas{left:0;top:1373px;width:1200px;height:426px;background:var(--grey);border-top:1px solid #ddd}
.areas-title{left:0;top:1475px;width:1200px;text-align:center;font-size:24px}
.area{width:130px;text-align:center;top:1538px}
.area-badge{width:104px;height:104px;margin:0 auto;border-radius:50%;background:var(--teal);border:5px solid #7fc9c4;display:flex;align-items:center;justify-content:center}
.area-badge.dark{background:var(--teal-dark)}
.area-label{margin-top:14px;font-size:12px;line-height:1.3;color:var(--muted)}

/* gallery */
.gallery{left:0;top:1799px;width:1200px;height:398px;background:var(--band)}
.gallery-title{left:0;top:1860px;width:1200px;text-align:center;color:#fff;font-size:24px}
.gallery-photo{top:1928px;width:252px;height:200px;box-shadow:0 12px 16px rgba(0,0,0,.3)}

/* footer */
.footer{left:0;top:2197px;width:1200px;height:192px;background:var(--footer)}
.footer-brand{left:96px;top:2230px;width:212px;height:118px;background:var(--teal);display:flex;align-items:center;justify-content:center;color:#fff;font-size:24px;font-weight:700;text-align:center;line-height:1.1}
.contact{left:783px;color:#fff;font-size:14px;line-height:1.35;display:flex;gap:16px;align-items:flex-start}
.contact svg{flex:none}
.legal{left:0;top:2389px;width:1200px;height:82px;background:var(--footer-deep)}
.legal-text{left:155px;top:2413px;color:#cfe6e4;font-size:10px;line-height:1.7;text-transform:uppercase}
.social{left:783px;top:2420px;display:flex;gap:14px}
.social span{width:20px;height:20px;border-radius:50%;background:#e6f2f1}
</style>
</head>
<body>

<div class="abs hero" role="img" aria-label="Bright drawing room with tall windows, draped curtains and a cushioned chaise"></div>
<div class="abs brand-box">Velmorra<br>Hangings</div>
<div class="abs top-phone">0300 555 0192</div>
<div class="abs top-mail">info@velmorrahangings.co.uk</div>
<nav class="abs nav">
  <span class="active">Home</span><span>About Us</span><span>News</span><span>Fabrics</span><span>Scatter Cushions &amp; Bed Throws</span><span>Gallery</span><span>Testimonials</span><span>Contact Us</span>
</nav>
<h1 class="abs headline">Double Your House for half the money</h1>
<p class="abs subline">See Our Curtains on lumen 6</p>

<div class="abs card card-side" style="left:151px">
  <h2 class="card-title" style="font-weight:400">Curtain Fabric types include</h2>
  <div class="card-photo" role="img" aria-label="Living room window dressed with cream curtains" style="background:linear-gradient(135deg,#d9cdb5,#a8936f)"></div>
  <p class="card-text">An expert in home measuring service and professional hanging.</p>
</div>
<div class="abs card card-mid">
  <h2 class="card-title" style="font-weight:400">Our Customers love us</h2>
  <div class="card-photo" role="img" aria-label="Portrait of a happy customer" style="background:linear-gradient(135deg,#e6d2c4,#8b6a58)"></div>
  <p class="card-name">Mrs K, Reading</p>
  <p class="card-text">The room is so much brighter now, and I love the contrasting cushions.<br><br>Thank you for your advice.</p>
</div>
<div class="abs card card-side" style="left:755px">
  <h2 class="card-title" style="font-weight:400">Our Latest Curtain and Fabric News</h2>
  <div class="card-photo" role="img" aria-label="Sheer white curtain beside a leafy plant" style="background:linear-gradient(135deg,#6f8f55,#e8ece6)"></div>
  <p class="card-text">We provide a made to measure curtain service.</p>
</div>

<section class="abs about">
  <h2 class="section-title" style="font-weight:400">Handmade Curtains</h2>
  <p>One of the many advantages of handmade curtains or made to measure curtains is that they fit perfectly and compliment the room. Often curtains that are purchased already made do not fit as they should and the end results reflect this.</p>
  <p>With handmade curtains or made to measure curtains obviously the style can be exactly as you choose with a wide range of different headers and linings available. Handmade curtains although more expensive than made to measure curtains have the advantage of no visible machine stitching.</p>
  <p>We carry sample handmade curtains and also made to measure curtains so you can study and see how they are manufactured. We have a extensive range of fabric from which our handmade curtains or made measure curtains can be produced from.</p>
</section>
<h2 class="abs section-title designer" style="font-weight:400">Meet Velmorra designer</h2>
<div class="abs video" role="img" aria-label="Video still of patterned curtains at a window"></div>
<svg class="abs" style="left:809px;top:1150px" width="60" height="42" viewBox="0 0 60 42"><rect width="60" height="42" rx="10" fill="#1b1b1b" opacity=".85"/><path d="M24 12 L40 21 L24 30 Z" fill="#fff"/></svg>
<div class="abs video-bar"></div>
<svg class="abs" style="left:662px;top:1287px" width="350" height="12" viewBox="0 0 350 12"><path d="M0 1 L8 6 L0 11 Z" fill="#ddd"/><rect x="20" y="4" width="16" height="4" fill="#aaa"/><text x="46" y="10" font-size="9" fill="#ccc" font-family="Arimo,sans-serif">0:00 / 6:57</text><rect x="300" y="2" width="14" height="8" fill="#888"/><rect x="330" y="2" width="14" height="8" fill="none" stroke="#ccc"/></svg>

<div class="abs areas"></div>
<h2 class="abs areas-title" style="font-weight:400">The areas we cover include</h2>
<div class="abs area" style="left:196px"><div class="area-badge"><svg width="46" height="40" viewBox="0 0 46 40" fill="#fff"><rect x="0" y="0" width="46" height="3"/><path d="M2 4 H14 C14 18 10 30 2 38 Z"/><path d="M44 4 H32 C32 18 36 30 44 38 Z"/><rect x="17" y="6" width="12" height="22" fill="none" stroke="#fff" stroke-width="2"/></svg></div><p class="area-label">Curtains<br>Berkshire</p></div>
<div class="abs area" style="left:319px"><div class="area-badge"><svg width="46" height="40" viewBox="0 0 46 40" fill="#fff"><rect x="0" y="0" width="46" height="3"/><path d="M2 4 H14 C14 18 10 30 2 38 Z"/><path d="M44 4 H32 C32 18 36 30 44 38 Z"/><rect x="17" y="6" width="12" height="22" fill="none" stroke="#fff" stroke-width="2"/></svg></div><p class="area-label">Curtains<br>Buckinghamshire</p></div>
<div class="abs area" style="left:451px"><div class="area-badge dark"><svg width="46" height="40" viewBox="0 0 46 40" fill="#fff"><rect x="0" y="0" width="46" height="3"/><path d="M2 4 H14 C14 18 10 30 2 38 Z"/><path d="M44 4 H32 C32 18 36 30 44 38 Z"/><rect x="17" y="6" width="12" height="22" fill="none" stroke="#fff" stroke-width="2"/></svg></div><p class="area-label">Curtains<br>Oxfordshire</p></div>
<div class="abs area" style="left:580px"><div class="area-badge"><svg width="46" height="40" viewBox="0 0 46 40" fill="#fff"><rect x="0" y="0" width="46" height="3"/><path d="M2 4 H14 C14 18 10 30 2 38 Z"/><path d="M44 4 H32 C32 18 36 30 44 38 Z"/><rect x="17" y="6" width="12" height="22" fill="none" stroke="#fff" stroke-width="2"/></svg></div><p class="area-label">Curtains<br>Winchester</p></div>
<div class="abs area" style="left:712px"><div class="area-badge"><svg width="46" height="40" viewBox="0 0 46 40" fill="#fff"><rect x="0" y="0" width="46" height="3"/><path d="M2 4 H14 C14 18 10 30 2 38 Z"/><path d="M44 4 H32 C32 18 36 30 44 38 Z"/><rect x="17" y="6" width="12" height="22" fill="none" stroke="#fff" stroke-width="2"/></svg></div><p class="area-label">Curtains<br>Guildford</p></div>
<div class="abs area" style="left:841px"><div class="area-badge"><svg width="46" height="40" viewBox="0 0 46 40" fill="#fff"><rect x="0" y="0" width="46" height="3"/><path d="M2 4 H14 C14 18 10 30 2 38 Z"/><path d="M44 4 H32 C32 18 36 30 44 38 Z"/><rect x="17" y="6" width="12" height="22" fill="none" stroke="#fff" stroke-width="2"/></svg></div><p class="area-label">Curtains<br>Oxford</p></div>

<div class="abs gallery"></div>
<h2 class="abs gallery-title" style="font-weight:400">Our Curtains Gallery</h2>
<div class="abs gallery-photo" style="left:60px;background:linear-gradient(135deg,#cbb993,#f1ece2)" role="img" aria-label="Sitting room with patterned curtains and white armchair"></div>
<div class="abs gallery-photo" style="left:338px;background:linear-gradient(135deg,#b08c5d,#6a4b2f)" role="img" aria-label="Dining room with golden curtains and table"></div>
<div class="abs gallery-photo" style="left:615px;background:linear-gradient(135deg,#ece6dc,#8a7b6a)" role="img" aria-label="Lounge with neutral curtains and ottoman"></div>
<div class="abs gallery-photo" style="left:892px;background:linear-gradient(135deg,#a98a66,#e7dccb)" role="img" aria-label="Bay window with cream curtains and sofa"></div>

<footer>
  <div class="abs footer"></div>
  <div class="abs footer-brand">Velmorra<br>Hangings</div>
  <div class="abs contact" style="top:2232px">
    <svg width="20" height="28" viewBox="0 0 20 28"><path d="M10 0 C4.5 0 0 4.5 0 10 C0 17 10 28 10 28 C10 28 20 17 20 10 C20 4.5 15.5 0 10 0 Z" fill="#fff"/><circle cx="10" cy="10" r="4" fill="var(--footer)"/></svg>
    <span>Velmorra Hangings,<br>14 Riverside Lane, Windsor,<br>Berkshire, SL4 2QX</span>
  </div>
  <div class="abs contact" style="top:2302px">
    <svg width="20" height="20" viewBox="0 0 20 20"><circle cx="10" cy="10" r="9" fill="none" stroke="#fff" stroke-width="2"/><path d="M6 5 L8 5 L9 8 L8 9 C8.6 10.6 9.4 11.4 11 12 L12 11 L15 12 L15 14 C10 15 5 10 6 5 Z" fill="#fff"/></svg>
    <span>0300 555 0192</span>
  </div>
  <div class="abs contact" style="top:2340px">
    <svg width="20" height="14" viewBox="0 0 20 14"><rect width="20" height="14" fill="#fff"/><path d="M0 0 L10 8 L20 0" fill="none" stroke="var(--footer)" stroke-width="1.5"/></svg>
    <span>info@velmorrahangings.co.uk</span>
  </div>
  <div class="abs legal"></div>
  <p class="abs legal-text">All rights reserved © Velmorra Hangings<br>Terms of use · Privacy policies · Cookies</p>
  <div class="abs social"><span></span><span></span><span></span><span></span><span></span><span></span></div>
</footer>

</body>
</html>
```